Local fast-growing company in the service sector

We are looking for a modern business card design, which should also appear on our letterheads

Target Market(s)

Private and industrial sectors

Contact Information for Business Card

Vorname Name
Lindkofer Str. 18
71468 Haldenbrunn
Tel.: 07163-418259-0
Name@kovaltec-pbz.de

Colors
9d9d9d
919191
aaaaaa

Requirements
Must have
• The logo (file) in silver

```html
<!DOCTYPE html>
<html lang="de">
<head>
<meta charset="utf-8">
<title>PBZ Visitenkarte</title>
<link href="https://fonts.googleapis.com/css2?family=Source+Sans+3:wght@400;600;700&display=swap" rel="stylesheet">
<style>
  :root {
    --stage: #3a3532;
    --card: #0b0b0b;
    --silver: #aaaaaa;
    --silver-mid: #9d9d9d;
    --silver-dark: #919191;
    --text: #e6e6e6;
    --rule: #2a2a2a;
  }
  * { margin: 0; padding: 0; box-sizing: border-box; }
  html, body { width: 1200px; height: 900px; overflow: hidden; }
  body {
    background: var(--stage);
    font-family: "Source Sans 3", "Myriad Pro", Arial, sans-serif;
    position: relative;
  }
  .card {
    position: absolute;
    top: 300px;
    width: 525px;
    height: 300px;
    background: var(--card);
    border-radius: 3px;
  }
  .card--back { left: 50px; }
  .card--front { left: 625px; }

  .brand-mark {
    position: absolute;
    display: flex;
    align-items: center;
    gap: 14px;
  }
  .brand-mark__square {
    width: 22px;
    height: 22px;
    background: var(--silver);
  }
  .brand-mark__name {
    color: var(--silver);
    font-weight: 700;
    letter-spacing: 2px;
  }
  .card--back .brand-mark { left: 70px; top: 110px; }
  .card--back .brand-mark__name { font-size: 64px; line-height: 1; }

  .divider {
    position: absolute;
    left: 300px;
    top: 40px;
    width: 1px;
    height: 220px;
    background: var(--rule);
  }
  .contact {
    position: absolute;
    left: 325px;
    top: 70px;
    color: var(--text);
    font-size: 14px;
    line-height: 19px;
  }
  .contact__name {
    font-weight: 600;
    font-size: 16px;
    letter-spacing: 0.5px;
    margin-bottom: 8px;
  }
  .contact__line { display: flex; align-items: center; gap: 7px; }
  .contact__line svg { width: 11px; height: 11px; fill: var(--silver); flex: none; }
  .contact__address { margin-top: 12px; }

  .card--front .brand-mark {
    left: 50%;
    top: 50%;
    transform: translate(-50%, -50%);
    flex-direction: column;
    align-items: flex-start;
    gap: 0;
  }
  .brand-row { display: flex; align-items: center; gap: 14px; }
  .card--front .brand-mark__name { font-size: 84px; line-height: 0.95; }
  .brand-mark__domain {
    color: var(--silver);
    font-weight: 700;
    font-size: 22px;
    letter-spacing: 1px;
    margin-left: 36px;
  }
</style>
</head>
<body>
  <section class="card card--back" aria-label="Kartenrückseite">
    <div class="brand-mark">
      <span class="brand-mark__square"></span>
      <span class="brand-mark__name">PBZ</span>
    </div>
    <div class="divider"></div>
    <div class="contact">
      <p class="contact__name">VORNAME NAME</p>
      <p class="contact__line">
        <svg viewBox="0 0 12 12" aria-hidden="true"><path d="M2.5 0.5 L4.5 0.5 L5.2 3.3 L3.8 4.4 Q5 7 7.6 8.2 L8.7 6.8 L11.5 7.5 L11.5 9.5 Q11.5 11.5 9.5 11.5 Q0.5 10.5 0.5 2.5 Q0.5 0.5 2.5 0.5Z"/></svg>
        07163-418259-0
      </p>
      <p class="contact__line">
        <svg viewBox="0 0 12 12" aria-hidden="true"><path d="M0 2 L12 2 L12 10 L0 10Z M0.8 2.6 L6 6.6 L11.2 2.6" fill="var(--silver)" stroke="#0b0b0b" stroke-width="0.9"/></svg>
        Name@kovaltec-pbz.de
      </p>
      <p class="contact__line">
        <svg viewBox="0 0 12 12" aria-hidden="true"><circle cx="6" cy="6" r="5.5"/><path d="M0.5 6 H11.5 M6 0.5 Q2.5 6 6 11.5 M6 0.5 Q9.5 6 6 11.5" stroke="#0b0b0b" stroke-width="0.8" fill="none"/></svg>
        www.kovaltec-pbz.de
      </p>
      <p class="contact__address">Lindkofer Str. 18<br>71468 Haldenbrunn</p>
    </div>
  </section>

  <section class="card card--front" aria-label="Kartenvorderseite">
    <div class="brand-mark">
      <div class="brand-row">
        <span class="brand-mark__square"></span>
        <span class="brand-mark__name">PBZ</span>
      </div>
      <span class="brand-mark__domain">kovaltec-pbz.de</span>
    </div>
  </section>
</body>
</html>
```